New Business Card Design Project

double sided business cards. i would like to design a business card with the logo attached . that logo being centered on 1 side and then my info on the other.

Boyd Whitfield CEO
Phone# 334-571-2806
Boyd@brightoakupkeep.com

Contact Information for Business Card

double sided one side the Logo attached below that saying Home Maintenance and Repair Specialists then on back my info Boyd Whitfield CEO Home Maintenance Specialist Phone# 334-571-2806 Boyd@brightoakupkeep.com

Font styles to use
Serif

Colors
0054AA
0677BA
7BADD7
CADEEF
E8F1F8
FFC000
F8CF3A
FAE287
FDF2CF
FEFAEE

Requirements
Must have
• double sided logo attached on one side with colors blue and gold. black background info on the other side

```html
<!DOCTYPE html>
<html lang="en">
<head>
<meta charset="utf-8">
<title>Bright Oak Upkeep – Business Card</title>
<link rel="stylesheet" href="https://fonts.googleapis.com/css2?family=Jost:wght@400;500&display=swap">
<style>
  :root {
    --backdrop: #b4b7bc;
    --card-black: #000000;
    --card-white: #ffffff;
    --brand-blue: #1677bd;
    --brand-gold: #ffc20e;
    --ink: #111111;
  }
  html, body {
    margin: 0;
    padding: 0;
    width: 1200px;
    height: 1000px;
    overflow: hidden;
    background: var(--backdrop);
    font-family: "Jost", "Futura", sans-serif;
  }
  .stage {
    position: relative;
    width: 1200px;
    height: 1000px;
  }
  .card {
    position: absolute;
    top: 352px;
    width: 466px;
    height: 301px;
    overflow: hidden;
  }
  .card--front {
    left: 97px;
    background: var(--card-black);
  }
  .card--back {
    left: 657px;
    background: var(--card-white);
  }
  .brand {
    position: absolute;
    left: 0;
    right: 0;
    top: 0;
    bottom: 0;
    display: flex;
    align-items: center;
    justify-content: center;
    gap: 14px;
  }
  .brand__square {
    width: 22px;
    height: 22px;
    background: var(--brand-gold);
  }
  .brand__name {
    color: var(--brand-blue);
    font-weight: 500;
    font-size: 30px;
    letter-spacing: 0.5px;
    text-transform: uppercase;
  }
  .contact {
    position: absolute;
    left: 32px;
    top: 78px;
  }
  .contact__name {
    margin: 0;
    color: var(--brand-blue);
    font-weight: 500;
    font-size: 27px;
    line-height: 1;
  }
  .contact__title {
    margin: 20px 0 0;
    color: var(--ink);
    font-size: 16px;
    letter-spacing: 1px;
    line-height: 1;
  }
  .contact__lines {
    margin: 22px 0 0;
    color: var(--ink);
    font-size: 14px;
    line-height: 19px;
    letter-spacing: 0.6px;
  }
  .accent {
    position: absolute;
    right: 0;
    bottom: 0;
  }
</style>
</head>
<body>
  <main class="stage">
    <section class="card card--front" aria-label="Card front">
      <div class="brand">
        <span class="brand__square"></span>
        <span class="brand__name">Bright Oak Upkeep</span>
      </div>
    </section>

    <section class="card card--back" aria-label="Card back">
      <div class="contact">
        <h1 class="contact__name">Boyd Whitfield</h1>
        <p class="contact__title">CEO</p>
        <p class="contact__lines">334-571-2806<br>Boyd@brightoakupkeep.com</p>
      </div>
      <svg class="accent" width="120" height="120" viewBox="0 0 120 120" aria-hidden="true">
        <rect x="40" y="40" width="80" height="80" fill="var(--brand-blue)"/>
      </svg>
    </section>
  </main>
</body>
</html>
```